Local massage therapist needs some new marketing material

Hi there! I am a massage therapist here in Denver, CO in Brindle Hollow(shopping and art district) of the city. My business is called Lunora Massage of Denver. My practice has an eastern influence and I do reflexology, thai massage and use Chinese herbs, etc. I know all my clients and pay close attention to details. I am also very respectful of tradition and it shows in how I work. I tend to like modern, clean, fun, Asian designs. I am wanting a new business card and brochure. I have a logo and branding for my business that I want used in the design. Currently, the sign for my building is purple and I think my logo was designed to be purple. I will attach pictures of it and can send whatever files are necessary so it can be integrated into the brochure, etc. I like the purple but open to using other colors as well. Thanks!
My website is lunoramassagestudio.example where info can be gathered about me and services/fees for brochure.
Updates

Just increased budget. Please see new feedback in discussion thread.

Thanks!

                                       HEY ALL,

Just wanted to let you know that I made a change to my website. It is on the Prices Page. I no longer have the frequent  flyer prices but I added discounts. Let me know if you have any questions. Thanks so much!

Target Market(s)

healthy, urban, educated, upper middle class, yogis

Industry/Entity Type

Marketing

Requirements
Must have
• logo stays purple
Should not have
• not too busy

```html
<!DOCTYPE html>
<html lang="en">
<head>
<meta charset="utf-8">
<title>Lunora Massage of Denver</title>
<link href="https://fonts.googleapis.com/css2?family=Raleway:wght@300;400&display=swap" rel="stylesheet">
<style>
  :root {
    --plum: #7a2a78;
    --brand-violet: #7030a0;
    --magenta: #8e2a72;
    --blush: #e3b3c4;
    --sage: #c8d6b4;
    --white: #ffffff;
    --photo-light: #e6e2cc;
    --photo-mid: #b3ab86;
    --photo-dark: #3c372a;
  }
  html, body {
    margin: 0;
    padding: 0;
    overflow: hidden;
    background: #ffffff;
  }
  .flyer {
    position: relative;
    width: 1200px;
    height: 839px;
    overflow: hidden;
    font-family: "Raleway", sans-serif;
    font-weight: 300;
  }
  .flyer__art {
    position: absolute;
    inset: 0;
  }
  .contact {
    position: absolute;
    top: 38px;
    left: 405px;
    width: 400px;
    text-align: center;
    color: var(--plum);
    font-size: 20px;
    line-height: 25px;
    text-shadow: 0 0 2px rgba(255,255,255,0.8);
  }
  .contact p { margin: 0; }
  .contact__group + .contact__group { margin-top: 25px; }
  .brand {
    position: absolute;
    top: 200px;
    left: 830px;
    width: 345px;
    text-align: center;
  }
  .brand__dot {
    width: 90px;
    height: 90px;
    margin: 0 auto 150px;
    border: 3px solid var(--brand-violet);
    border-radius: 50%;
  }
  .brand__name {
    margin: 0;
    color: var(--brand-violet);
    font-weight: 300;
    font-size: 58px;
    letter-spacing: 10px;
    line-height: 1;
  }
  .tagline {
    position: absolute;
    left: 830px;
    width: 350px;
    text-align: center;
    color: var(--white);
    font-size: 29px;
    line-height: 28px;
    margin: 0;
  }
  .tagline--main { top: 697px; }
  .tagline--end { top: 798px; }
</style>
</head>
<body>
<main class="flyer">
  <svg class="flyer__art" width="1200" height="839" viewBox="0 0 1200 839" aria-hidden="false">
    <defs>
      <linearGradient id="photoTone" x1="0" y1="0" x2="1" y2="1">
        <stop offset="0" stop-color="var(--photo-mid)"/>
        <stop offset="0.55" stop-color="var(--photo-light)"/>
        <stop offset="1" stop-color="var(--photo-mid)"/>
      </linearGradient>
      <linearGradient id="floorTone" x1="0" y1="0" x2="0" y2="1">
        <stop offset="0" stop-color="var(--photo-mid)" stop-opacity="0"/>
        <stop offset="1" stop-color="var(--photo-dark)"/>
      </linearGradient>
    </defs>
    <g class="backdrop" role="img" aria-label="Photo of stacked smooth massage stones on a bamboo mat in front of soft bamboo stalks">
      <rect width="1200" height="839" fill="url(#photoTone)"/>
      <rect y="560" width="1200" height="279" fill="url(#floorTone)"/>
    </g>
    <path class="wave wave--blush" d="M0 8 C300 20 500 250 760 470 C950 620 1100 600 1200 560 L1200 610 C1080 660 920 680 720 520 C480 320 280 60 0 48 Z" fill="var(--blush)" opacity="0.85"/>
    <path class="wave wave--magenta" d="M0 92 C250 110 420 260 600 420 C780 580 980 650 1200 640 L1200 740 C960 740 760 650 560 480 C380 320 220 110 0 100 Z" fill="var(--magenta)" opacity="0.85"/>
    <path class="wave wave--white" d="M0 308 C300 360 520 620 800 720 C950 770 1100 775 1200 765" fill="none" stroke="var(--white)" stroke-width="6" opacity="0.7"/>
    <path class="wave wave--sage" d="M0 548 C180 470 380 520 560 640 C700 730 780 800 860 839 L0 839 Z" fill="var(--sage)" opacity="0.75"/>
    <path class="band band--footer" d="M640 655 L1200 655 L1200 775 C1000 790 820 770 640 700 Z" fill="var(--magenta)" opacity="0.7"/>
  </svg>

  <section class="contact">
    <div class="contact__group">
      <p>1487 E Larkspur Ave, Denver, CO 80218</p>
      <p>P: 303.555.0187</p>
      <p>E: info@lunoramassagestudio.example</p>
    </div>
    <div class="contact__group">
      <p>Tues - Fri 10am - 8pm Sat</p>
      <p>10am-5pm</p>
    </div>
    <div class="contact__group">
      <p>(Appointments required)</p>
      <p>No walk-ins please.</p>
    </div>
  </section>

  <div class="brand">
    <div class="brand__dot"></div>
    <h1 class="brand__name">LUNORA</h1>
  </div>

  <p class="tagline tagline--main">YOUR PATH TO<br>WELLNESS</p>
  <p class="tagline tagline--end">BEGINS HERE!</p>
</main>
</body>
</html>
```